Business Card Design needed for logo design project

We need a business card design for a construction parts business.

We would like our main company logo on the front of the card and have our other company website logo on the rear of the card.

Both logos will be attached.

Front of card
Logo is KTR
Can we also have the wording "Construction Equipment Parts Specialists"
Main details to include:

Address:
Telephone:
Mobile:
Email:
Website:

Rear of card.

Logo is gearvaultdepot.com.au (we would like this logo taking up the most of the rear)
Also we want under gearvaultdepot.com.au the following wording "Parts Sourced For You From Across The Globe"
Updates

Please see new update for our design

Target Market(s)

Construction Industry.
Earthmoving Equipment owners.

Industry/Entity Type

Construction

Font styles to use
Sans Serif

Requirements
Must have
• Easy to read.
Clean and smart.
Should not have
• Should not have any colours other than the colours of our logos.

```html
<!DOCTYPE html>
<html lang="en">
<head>
<meta charset="utf-8">
<title>KTR Business Card</title>
<link href="https://fonts.googleapis.com/css2?family=Oswald:wght@500;700&family=Arimo:wght@400;700&display=swap" rel="stylesheet">
<style>
  :root {
    --navy: #0d2740;
    --teal: #3d8ea8;
    --ink: #2b3a4a;
    --card-white: #f7f7f7;
    --backdrop: #e9eaec;
  }
  * { margin: 0; padding: 0; box-sizing: border-box; }
  html, body { width: 1200px; height: 900px; overflow: hidden; }
  body {
    background: var(--backdrop);
    font-family: "Arimo", Arial, sans-serif;
    color: var(--ink);
    position: relative;
  }
  .card {
    position: absolute;
    left: 350px;
    width: 500px;
    height: 286px;
    border-radius: 3px;
    box-shadow: 0 6px 18px rgba(0,0,0,0.12);
  }
  .card-front { top: 140px; background: var(--card-white); padding: 34px 38px; }
  .card-back { top: 476px; background: var(--navy); display: flex; flex-direction: column; align-items: center; justify-content: center; }

  .brand { display: flex; align-items: center; gap: 10px; }
  .brand-name {
    font-family: "Oswald", Arial, sans-serif;
    font-weight: 700;
    font-size: 46px;
    line-height: 1;
    color: var(--navy);
    letter-spacing: 1px;
  }
  .brand-dot { width: 26px; height: 26px; border-radius: 50%; background: var(--teal); }
  .brand-tagline {
    margin-top: 6px;
    font-size: 7.5px;
    letter-spacing: 1.2px;
    text-transform: uppercase;
    color: var(--teal);
  }
  .person { margin-top: 20px; }
  .person-name { font-size: 14px; font-weight: 700; color: var(--navy); letter-spacing: 0.5px; }
  .person-role { font-size: 10px; margin-top: 2px; }
  .contact-list { list-style: none; margin-top: 12px; font-size: 10.5px; }
  .contact-list li { display: flex; align-items: center; gap: 8px; margin-bottom: 5px; }
  .contact-list svg { width: 10px; height: 10px; fill: var(--teal); flex: none; }
  .contact-address { margin-top: 6px; font-size: 10.5px; }
  .social-row { position: absolute; right: 24px; top: 30px; display: flex; gap: 3px; }
  .social-row span { width: 11px; height: 11px; background: var(--teal); }

  .site-name {
    font-family: "Oswald", Arial, sans-serif;
    font-weight: 500;
    font-size: 38px;
    color: #ffffff;
    letter-spacing: 0.5px;
    display: flex;
    align-items: center;
    gap: 12px;
  }
  .site-dot { width: 34px; height: 34px; border-radius: 50%; background: var(--teal); }
  .site-tagline {
    margin-top: 6px;
    font-size: 9px;
    letter-spacing: 1.6px;
    text-transform: uppercase;
    color: var(--teal);
    margin-right: 46px;
  }
</style>
</head>
<body>
  <section class="card card-front">
    <div class="brand">
      <span class="brand-name">KTR</span>
      <span class="brand-dot"></span>
    </div>
    <p class="brand-tagline">Construction Equipment Parts Specialists</p>

    <div class="person">
      <p class="person-name">DANIEL REYES</p>
      <p class="person-role">President</p>
    </div>

    <ul class="contact-list">
      <li>
        <svg viewBox="0 0 10 10"><rect x="2.5" y="0.5" width="5" height="9" rx="1"/></svg>
        041.555.0192
      </li>
      <li>
        <svg viewBox="0 0 10 10"><path d="M2 0.5 L4 0.5 L4.5 3 L3.2 4 Q4.5 6.3 6 6.8 L7 5.5 L9.5 6 L9.5 8 Q9.5 9.5 8 9.5 Q1 9 0.5 2 Q0.5 0.5 2 0.5Z"/></svg>
        027.555.0148
      </li>
      <li>
        <svg viewBox="0 0 10 10"><path d="M0.5 2 H9.5 V8.5 H0.5Z M0.5 2 L5 5.5 L9.5 2" /></svg>
        info@gearvaultdepot.com.au
      </li>
    </ul>
    <p class="contact-address">PO Box 402, Ashford, AU 54321</p>

    <div class="social-row" aria-hidden="true"><span></span><span></span><span></span></div>
  </section>

  <section class="card card-back">
    <p class="site-name">GEARVAULTDEPOT.COM.AU <span class="site-dot"></span></p>
    <p class="site-tagline">Parts Sourced For You From Across The Globe</p>
  </section>
</body>
</html>
```